San Francisco Leading Consulting firm - 47Nova Web Design Project

•Create a Web Design
•Uncoded webpage layout design
•2 Pages Design - Homepage + Interior Page

Task Description
Hello, we're looking for a re-design our current website www.47nova-example.com

we have a sample mockup design @

http://47nova.civicpane-example.org/

This shows the layout that we like and also a sample of 6 pictures that would change based on where you mouse over..

6 pictures HOME design needs to be included.

SMART
THOUGHTFUL
FLEXIBLE
CREATIVE SERVICES
TECHNICAL SERVICES
PARTNERS

sites we like:

http://www.brelmoradvisory-example.com/Home.cfm?id=Home
http://www.pixelquarry-example.com/index.html

Our company can be best described as: 100+ employees, cutting-edge, depandable, innovative, strong, smart.

Our Primary focus is: IT Consulting Services and Creative Design services

47Nova LLC is a consulting firm providing creative design, business and technology solutions to both private and public interests.

Established in 1996, 47Nova is a San Francisco based company providing specialists for a range of business needs including:

Creative Design Services
•Print
•Logo Design
•Website Design
•Illustration

and

Business and Technology solutions

•Application Software and Web Development
•Business Process Re-Design (BPR)
•Business/Systems Analysis and Requirement Documentation
•Mentoring and Training
•Network/Hardware Installation Services
•System Design and Architecture
•Vendor Management
•Teamvault Architecture and Implementation

our sample mockup site:

Reason: Due to holiday season, we're not available to work with designers and finilize our design.  

Thank you very much for submitting your design.

We appreciate your time and creativity.   Since, our office is currently closed for holidays, we will be reviewing it in details next week and will make our decision as soon as possible.

It would be great if you could submit any of your changes by Wed next week, so it would be part of our reviews. 

Please see updated wireframe under attachments:  we have some minor updates to our wireframe that we would like you to update your designs, if possible.  

We also encorouge you not to use our standard wireframe and come up with more unique designs.   Everything would be considered when we review your design.

 

Target Market(s)

Creative services and professional services clients, including government agencies

Industry/Entity Type

Business

Requirements
Must have
• Clean, professional look, easy navigation

```html
<!DOCTYPE html>
<html lang="en">
<head>
<meta charset="utf-8">
<title>Contact 47Nova</title>
<link rel="stylesheet" href="https://fonts.googleapis.com/css2?family=Questrial&family=Tinos:wght@400;700&family=Arimo:wght@700&display=swap">
<style>
  :root {
    --frame-blue: #3d82c6;
    --header-light: #f2f2f4;
    --header-mid: #dcdde2;
    --logo-grey: #5b5d63;
    --nav-dark: #252f5c;
    --nav-mid: #3b4a80;
    --nav-text: #8fd0ff;
    --tab-active: #ffffff;
    --tab-active-text: #d0202a;
    --hero-black: #050505;
    --capsule-light: #cfd0d2;
    --capsule-dark: #2a2a2a;
    --accent-blue: #4a90c8;
    --contact-text: #4f80b2;
    --link-blue: #0000ee;
    --panel-light: #e9ebee;
    --panel-mid: #c6cad0;
    --silver-light: #fbfbfb;
    --silver-dark: #9a9ca0;
    --footer-black: #000000;
    --footer-text: #ffffff;
  }
  * { margin: 0; padding: 0; box-sizing: border-box; }
  html, body { width: 866px; height: 1200px; overflow: hidden; }
  body { background: var(--frame-blue); font-family: "Tinos", "Times New Roman", serif; position: relative; }

  .page { position: absolute; left: 14px; top: 14px; width: 838px; height: 1172px; background: var(--panel-light); overflow: hidden; }

  .site-header { position: absolute; left: 0; top: 0; width: 838px; height: 152px;
    background: linear-gradient(90deg, var(--header-mid) 0%, var(--header-light) 45%, var(--header-light) 100%); }
  .brand { position: absolute; left: 52px; top: 70px; display: flex; align-items: center; gap: 16px; }
  .brand-mark { width: 34px; height: 34px; border-radius: 50%; background: var(--accent-blue); }
  .brand-name { font-family: "Questrial", "Helvetica", sans-serif; font-size: 56px; color: var(--logo-grey); letter-spacing: 2px; line-height: 1; }

  .main-nav { position: absolute; left: 0; top: 152px; width: 838px; height: 19px;
    background: linear-gradient(180deg, var(--nav-mid), var(--nav-dark)); }
  .main-nav a { position: absolute; top: 0; height: 19px; line-height: 19px; font-family: "Arimo", Arial, sans-serif; font-weight: 700;
    font-size: 8.5px; color: var(--nav-text); text-decoration: none; letter-spacing: 0.3px; }
  .main-nav a.is-active { background: var(--tab-active); color: var(--tab-active-text); width: 77px; text-align: center; left: 0; }

  .hero { position: absolute; left: 0; top: 171px; width: 838px; height: 226px; background: #ffffff; }
  .hero-frame { position: absolute; left: 3px; top: 7px; width: 832px; height: 215px; border-radius: 28px; background: var(--hero-black); }
  .hero-capsule { position: absolute; left: 41px; top: 36px; width: 750px; height: 144px; border-radius: 72px;
    background: radial-gradient(ellipse 45% 80% at 50% 40%, var(--capsule-light) 0%, #8d8e90 45%, var(--capsule-dark) 100%); }
  .hero-title { position: absolute; left: 0; right: 0; top: 184px; text-align: center; font-size: 19px; color: var(--accent-blue); }

  .divider { position: absolute; left: 0; width: 838px;
    background: linear-gradient(180deg, var(--silver-dark) 0%, var(--silver-light) 40%, var(--silver-light) 60%, var(--silver-dark) 100%); }

  .panel { position: absolute; left: 0; width: 838px;
    background: radial-gradient(ellipse 60% 75% at 38% 35%, #f6f7f8 0%, var(--panel-light) 45%, var(--panel-mid) 100%); }

  .contact-details { position: absolute; left: 0; right: 0; top: 52px; text-align: center; color: var(--contact-text); font-size: 13.5px; }
  .contact-details p { height: 34.5px; }
  .contact-details strong { font-weight: 700; }

  .contact-banner { position: absolute; left: 0; right: 0; top: 140px; text-align: center; font-size: 86px; color: var(--accent-blue); line-height: 1; }
  .contact-banner a { color: var(--link-blue); text-decoration: underline; text-decoration-thickness: 2px; text-underline-offset: 6px; }

  .site-footer { position: absolute; left: 0; top: 1139px; width: 838px; height: 28px; background: var(--footer-black);
    color: var(--footer-text); font-size: 12px; text-align: center; line-height: 26px; }
</style>
</head>
<body>
  <div class="page">
    <header class="site-header">
      <div class="brand">
        <span class="brand-mark"></span>
        <span class="brand-name">47NOVA</span>
      </div>
    </header>

    <nav class="main-nav">
      <a class="is-active" href="#">HOME</a>
      <a style="left:97px" href="#">COMPANY</a>
      <a style="left:165px" href="#">TECHNICAL SERVICES</a>
      <a style="left:275px" href="#">CREATIVE SERVICES</a>
      <a style="left:389px" href="#">PARTNERS</a>
      <a style="left:465px" href="#">CONTACT US</a>
    </nav>

    <section class="hero">
      <div class="hero-frame">
        <div class="hero-capsule" role="img" aria-label="Photograph of downtown office towers rising into a grey sky"></div>
      </div>
      <h1 class="hero-title">Contact 47Nova</h1>
    </section>

    <div class="divider" style="top:397px; height:14px;"></div>

    <section class="panel" style="top:411px; height:337px;" role="img" aria-label="Soft grey background with flowing curved light bands">
      <div class="contact-details">
        <p>47Nova, LLC</p>
        <p>2250 Harbor Row, Suite 410</p>
        <p>San Francisco, CA 94111</p>
        <p>Phone: <strong>1-415-555-0148</strong></p>
        <p>Fax: <strong>1-415-555-0162</strong></p>
      </div>
    </section>

    <div class="divider" style="top:748px; height:12px;"></div>
    <div class="divider" style="top:767px; height:17px;"></div>

    <section class="panel" style="top:784px; height:343px;" role="img" aria-label="Soft grey background with flowing curved light bands">
      <p class="contact-banner">Contact <a href="#">47Nova</a></p>
    </section>

    <div class="divider" style="top:1127px; height:12px;"></div>

    <footer class="site-footer">Copyright 2010, 47Nova, LLC All rights reserved.</footer>
  </div>
</body>
</html>
```